Custom Framing Shop Stonebrook Framing Studio

I want an eye catching graphic that will be used a s business sign on a busy road. The sign MUST communicate the type of business it is clearly to vehicles traveling at 40 mph. This is a custom picture framing business and the sign will be hanging and be approximately 32" X 48". The business name is Stonebrook Framing Studio; Custom framing: by appointment and should include a whole or partial image of a picture frame as a visual que. I've included inspiration idea's, color pallets and styles that I like and a current business card for inspiration. I like the crimson font style shadowing and background colors of the attached Pello's pizzeria sign. I'd prefer crimson letters. Custom Framing is the message to communicate, followed by phone number and business name. I like the idea of a shield shape with a banner since it would more eye catching, Once again the Stonebrook image and name is less important than communicating what the business does. I like Crimson, grey, gold, black but am open to new ideas . I like the idea of a shield with a banner more than a rectangle, but am open to idea's

Target Market(s)

My target market is local homeowners ($700k+) who want a relationship with their framer and are willing to pay for a customized experience compared to a craft store experience. I have more female clients then men.

Industry/Entity Type

Picture Framing Art

Other font styles liked:
• Look at the attached image of a custom pizzeria sign, its kid of a custom car pinstripe font style. Script and decorative may be difficult to read while driving by but add to the elegance.

Colors

Designer to choose colors to be used in the design.

Requirements
Must have
• Clearly communicate what the business does "Custom framing" preferably with a picture frame and words
Nice to have
• incorporate a Stonebrook into the graphic
Should not have
• A Stonebrook image doesn't communicate what the business does to a vehicle traveling at 40 mph by the sign

```html
<!DOCTYPE html>
<html lang="en">
<head>
<meta charset="utf-8">
<title>Stonebrook Framing Studio – Hanging Sign</title>
<link rel="stylesheet" href="https://fonts.googleapis.com/css2?family=Montserrat:wght@700;800&family=Fira+Sans:wght@500&family=Oswald:wght@600;700&display=swap">
<style>
  :root {
    --crimson: #8c1620;
    --cream: #ead5b0;
    --ink: #1f1f1f;
    --flourish: #3a3430;
    --backdrop: #e9e7e3;
  }
  html, body {
    margin: 0;
    padding: 0;
    width: 1200px;
    height: 952px;
    overflow: hidden;
    background: var(--backdrop);
  }
  .sign {
    display: block;
    width: 1200px;
    height: 952px;
  }
  .sign__name {
    font-family: "Montserrat", sans-serif;
    font-weight: 800;
    fill: var(--ink);
  }
  .sign__subtitle {
    font-family: "Fira Sans", sans-serif;
    font-weight: 500;
    fill: var(--ink);
  }
  .sign__banner-text {
    font-family: "Oswald", sans-serif;
    font-weight: 700;
  }
  .sign__banner-text--shadow { fill: var(--ink); }
  .sign__banner-text--face { fill: var(--cream); }
  .sign__appointment {
    font-family: "Montserrat", sans-serif;
    font-weight: 700;
    fill: var(--ink);
  }
  .sign__phone {
    font-family: "Oswald", sans-serif;
    font-weight: 700;
    fill: var(--crimson);
  }
</style>
</head>
<body>
<svg class="sign" viewBox="340 235 1550 1230" preserveAspectRatio="xMidYMid meet" xmlns="http://www.w3.org/2000/svg" role="img" aria-label="Stonebrook Framing Studio shield sign: Custom Framing, by appointment">
  <defs>
    <path id="shield-shape" d="M685,392 Q800,385 830,335 Q1115,205 1400,335 Q1430,385 1545,392 L1545,1268 Q1440,1275 1420,1318 L1115,1458 L810,1318 Q790,1275 685,1268 Z"/>
    <clipPath id="shield-clip"><use href="#shield-shape"/></clipPath>
  </defs>

  <g class="sign__shield">
    <use href="#shield-shape" fill="var(--cream)"/>
    <g clip-path="url(#shield-clip)" fill="none">
      <use href="#shield-shape" stroke="var(--ink)" stroke-width="96"/>
      <use href="#shield-shape" stroke="var(--crimson)" stroke-width="72"/>
      <use href="#shield-shape" stroke="var(--cream)" stroke-width="16"/>
    </g>
  </g>

  <text class="sign__name" x="1115" y="572" font-size="138" text-anchor="middle" textLength="700" lengthAdjust="spacingAndGlyphs">STONEBROOK</text>
  <text class="sign__subtitle" x="1122" y="676" font-size="68" text-anchor="middle" textLength="525" lengthAdjust="spacing">Framing Studio</text>

  <g class="sign__banner">
    <path d="M662,782 L800,752 L806,768 Q1115,738 1414,768 L1420,745 L1562,777 Q1588,872 1566,972 Q1115,930 664,980 Q640,882 662,782 Z"
          fill="var(--crimson)" stroke="var(--ink)" stroke-width="12" stroke-linejoin="round"/>
    <path d="M682,796 L808,772 Q1115,752 1410,782 L1545,792" fill="none" stroke="var(--cream)" stroke-width="6"/>
    <path d="M684,962 Q1115,918 1550,958" fill="none" stroke="var(--cream)" stroke-width="6"/>
    <text class="sign__banner-text sign__banner-text--shadow" x="1122" y="942" font-size="178" text-anchor="middle" textLength="830" lengthAdjust="spacingAndGlyphs">CUSTOM FRAMING</text>
    <text class="sign__banner-text sign__banner-text--face" x="1112" y="932" font-size="178" text-anchor="middle" textLength="830" lengthAdjust="spacingAndGlyphs">CUSTOM FRAMING</text>
  </g>

  <g class="sign__appointment-line">
    <line x1="787" y1="1043" x2="840" y2="1043" stroke="var(--crimson)" stroke-width="5"/>
    <text class="sign__appointment" x="1116" y="1058" font-size="44" text-anchor="middle" textLength="498" lengthAdjust="spacing">BY APPOINTMENT</text>
    <line x1="1388" y1="1043" x2="1440" y2="1043" stroke="var(--crimson)" stroke-width="5"/>
  </g>

  <text class="sign__phone" x="1113" y="1190" font-size="130" text-anchor="middle" textLength="682" lengthAdjust="spacingAndGlyphs">360-555-0147</text>

  <g class="sign__divider">
    <line x1="935" y1="1246" x2="1275" y2="1246" stroke="var(--ink)" stroke-width="4"/>
    <rect x="1025" y="1232" width="160" height="96" rx="40" fill="var(--flourish)" role="img" aria-label="Decorative scroll flourish"/>
  </g>
</svg>
</body>
</html>
```